Car Dealership Showroom Poster

Design a 3'x5' poster (portiat layout) to advertise our 36 month / 36,000 mile warranty.

Below is a link to our website for color / logo and program details.

https://brakewellautosnj.com/

https://brakewellautosnj.com/36-month-36000-mile-limited-warranty

https://brakewellautosnj.com/36-month-36000-mile-limited-warranty/

```html
<!DOCTYPE html>
<html lang="en">
<head>
<meta charset="utf-8">
<title>Brakewell Autos – 36 Month / 36,000 Mile Warranty</title>
<link rel="stylesheet" href="https://fonts.googleapis.com/css2?family=Figtree:ital,wght@0,800;1,700;1,800&display=swap">
<style>
  :root {
    --paper: #f2f2f2;
    --green: #0b6b36;
    --green-mid: #23794b;
    --green-deep: #0a4f28;
    --green-bright: #1e9a4c;
    --grey: #8f8f93;
    --grey-swoosh: #939396;
    --white: #ffffff;
    --gold: #c9a13e;
  }
  * { margin: 0; padding: 0; box-sizing: border-box; }
  html, body { width: 840px; height: 1200px; overflow: hidden; background: var(--paper); }
  .poster {
    position: relative;
    width: 840px;
    height: 1200px;
    background: var(--paper);
    overflow: hidden;
    font-family: "Figtree", "Helvetica Neue", Arial, sans-serif;
  }
  .backdrop { position: absolute; inset: 0; width: 840px; height: 1200px; }

  .brand {
    position: absolute;
    left: 82px;
    top: 52px;
    color: var(--green);
    font-weight: 800;
    line-height: 1;
  }
  .brand-name { font-size: 72px; letter-spacing: -1px; display: block; }
  .brand-sub {
    display: flex;
    align-items: center;
    gap: 16px;
    margin-top: 6px;
    margin-left: 68px;
    font-size: 40px;
    letter-spacing: 14px;
  }
  .brand-dot { width: 34px; height: 34px; border-radius: 50%; background: var(--green); }

  .tagline {
    position: absolute;
    left: 36px;
    top: 208px;
    width: 650px;
    height: 63px;
    display: flex;
    align-items: center;
    color: var(--white);
    font-style: italic;
    font-weight: 800;
    font-size: 22.5px;
    letter-spacing: 0;
    white-space: nowrap;
  }

  .benefits {
    position: absolute;
    left: 67px;
    top: 338px;
    width: 680px;
    list-style: none;
  }
  .benefit { margin-bottom: 12px; }
  .benefit h2 {
    color: var(--green);
    font-style: italic;
    font-weight: 800;
    font-size: 25px;
    line-height: 30px;
  }
  .benefit p {
    margin-top: 4px;
    padding-left: 19px;
    width: 665px;
    color: var(--grey);
    font-style: italic;
    font-weight: 700;
    font-size: 19.4px;
    line-height: 25px;
  }

  .seal {
    position: absolute;
    left: 476px;
    top: 756px;
    width: 334px;
    height: 334px;
    border-radius: 50%;
    background: radial-gradient(circle at 50% 45%, var(--green-bright) 0%, var(--green-deep) 62%, var(--gold) 63%, #9c7424 100%);
  }
</style>
</head>
<body>
<main class="poster">
  <svg class="backdrop" viewBox="0 0 840 1200" aria-hidden="true">
    <path class="swoosh-grey" fill="var(--grey-swoosh)" d="M783,0 C802,180 785,380 740,507 C805,350 840,200 840,60 L840,0 Z"/>
    <path class="field-green" fill="var(--green-mid)" d="M840,355 C800,600 700,800 560,950 C480,1030 380,1100 260,1200 L840,1200 Z"/>
    <path class="wedge-green" fill="var(--green)" d="M0,1110 C180,1102 320,1062 420,1002 C320,1082 200,1160 110,1200 L0,1200 Z"/>
    <path class="swoosh-line" fill="var(--grey-swoosh)" d="M465,1200 C540,1130 620,1085 700,1060 C630,1095 560,1140 500,1200 Z"/>
    <path class="swoosh-white" fill="var(--white)" d="M448,1200 C520,1080 680,990 840,930 L840,958 C690,1010 560,1090 490,1200 Z"/>
    <path class="swoosh-white" fill="var(--white)" d="M570,1200 C650,1120 740,1075 840,1062 L840,1078 C745,1095 660,1140 600,1200 Z"/>
    <path class="tagline-band" fill="var(--green)" d="M0,208 L712,208 Q722,208 719,218 L705,262 Q702,271 692,271 L0,271 Z"/>
  </svg>

  <header class="brand">
    <span class="brand-name">BRAKEWELL</span>
    <span class="brand-sub"><span class="brand-dot"></span>AUTOS</span>
  </header>

  <div class="tagline">DRIVE WITH CONFIDENCE, PROTECTED BY BRAKEWELL</div>

  <ul class="benefits">
    <li class="benefit">
      <h2>Comprehensive Coverage:</h2>
      <p>Peace-of-mind protection on engine, transmission, drivetrain, and<br>more for 3 years or 36,000 miles—whichever comes first.</p>
    </li>
    <li class="benefit">
      <h2>No Surprise Costs:</h2>
      <p>Major covered repairs are handled at no additional cost to you.<br>Just pay a small deductible.</p>
    </li>
    <li class="benefit">
      <h2>Certified Quality:</h2>
      <p>This warranty reflects our confidence in the quality of our vehicles.<br>We stand behind what we sell.</p>
    </li>
    <li class="benefit">
      <h2>Hassle-Free Service:</h2>
      <p>Warranty repairs can be completed at our state-of-the-art service<br>center for your convenience.</p>
    </li>
    <li class="benefit">
      <h2>Transferable Value:</h2>
      <p>Enhances your vehicle's resale value, offering<br>a great selling point for future buyers.</p>
    </li>
  </ul>

  <div class="seal" role="img" aria-label="Gold and green warranty seal badge: 36 months, 36,000 mile warranty, we've got you covered"></div>
</main>
</body>
</html>
```